Creative Web Design - Intl Market Research Company

We need an innovative web design for an emerging company into the international market research marketplace.

The company, Velmoran Associates, is a Trade, Investment, and Market Research company. Velmoran offers domestic and international companies increased success in the U.S. marketplace by providing a variety of services. (seen on attached brochure)

The website should be cutting edge and creative while having an easy navigation. The color is not fixed and attached logo is not finalized, feel free to post anything from conservative to progressive options. Keep in mind target customers are domestic and international businesses looking to emerge/improve in the U.S. marketplace.

Additional Company information is located in the attached documentation. The documentation is outdated & winner will have priority standing for our next projects.(logo & document re-design)
Updates

I have received a few e-mail requests and have updated the status to guaranteed payment.

Thanks!

Target Market(s)

Any company, foreign and domestic, looking to introduce their product into the U.S. marketplace.

Industry/Entity Type

Market Research

Requirements
Must have
• Easy Navigation
Should not have
• Too many buttons
Difficult navigation
Excessive Typography

```html
<!DOCTYPE html>
<html lang="en">
<head>
<meta charset="utf-8">
<title>Velmoran Associates</title>
<link href="https://fonts.googleapis.com/css2?family=Questrial&family=Arimo:wght@400&display=swap" rel="stylesheet">
<style>
:root{
  --green:#8cbf26;
  --ink:#111;
  --text:#555;
  --muted:#888;
  --rule:#dcdcdc;
  --footer:#f2f2f2;
}
*{margin:0;padding:0;box-sizing:border-box}
html,body{width:1200px;height:958px;overflow:hidden;background:#fff}
body{position:relative;font-family:"Questrial",sans-serif;color:var(--ink)}
a{color:inherit;text-decoration:none}
.abs{position:absolute}

.site-header{position:absolute;left:0;top:0;width:1200px;height:108px;border-bottom:1px solid #e2e2e2;box-shadow:0 1px 3px rgba(0,0,0,.06)}
.brand{position:absolute;left:200px;font-family:"Questrial",sans-serif;color:var(--ink);font-size:30px;line-height:32px;white-space:nowrap}
.brand--header{top:14px}
.brand--footer{top:884px;font-size:27px;line-height:29px}
.socials{left:764px;top:16px;display:flex;gap:6px}
.socials span{width:20px;height:20px;border-radius:50%;background:#444;display:block}
.search{left:846px;top:14px;width:154px;height:24px;border:1px solid #ccc;font-family:"Arimo",sans-serif;font-style:italic;font-size:10px;color:#999;padding:5px 5px}
.search svg{position:absolute;right:3px;top:3px}
.search::before{content:"";position:absolute;right:24px;top:3px;width:1px;height:16px;background:#ccc}
.nav-rule{left:474px;top:66px;width:526px;height:1px;background:#ccc}
.nav{display:flex;align-items:center;justify-content:space-between;width:526px;font-family:"Arimo",sans-serif;font-size:11.5px;color:#333;white-space:nowrap}
.nav a{line-height:12px;white-space:nowrap}
.nav .sep{width:0;height:12px;border-left:1px dotted #999}
.nav .active{color:var(--green)}
.nav--header{left:474px;top:80px}
.nav--footer{left:474px;top:899px}

.hero{left:0;top:109px;width:1200px;height:388px;background:radial-gradient(ellipse at 50% 45%,#ffffff 0%,#f3f3f3 45%,#d9d9d9 100%)}
.hero-title{left:316px;top:162px;font-size:47px;line-height:42px;letter-spacing:-.5px;white-space:nowrap}
.hero-title .accent{color:var(--green);display:block}
.hero-art{left:300px;top:138px;width:600px;height:334px}
.hero-shadow{left:200px;top:482px;width:800px;height:6px;background:radial-gradient(ellipse at center,rgba(0,0,0,.25),rgba(0,0,0,0) 70%)}
.arrow{top:236px}

.welcome{left:200px;top:520px;width:490px}
.welcome h1{font-weight:400;font-size:23px;color:#aaa;margin-bottom:8px;white-space:nowrap}
.welcome h1 .name{color:var(--ink)}
.welcome h1 .name em{font-style:normal;color:var(--green)}
.copy{font-family:"Arimo",sans-serif;font-size:9.6px;line-height:14.4px;color:var(--text)}
.split{left:703px;top:534px;width:1px;height:85px;background:var(--rule)}
.quote{left:712px;top:541px;width:296px;text-align:center;font-size:23px;line-height:23px;white-space:nowrap}
.band-rule{left:0;top:638px;width:1200px;height:1px;background:var(--rule)}

.news-title{left:200px;top:666px;font-size:22px;font-weight:400}
.news-item{top:718px;width:200px}
.news-item .date{font-size:19px;color:#777;line-height:22px}
.news-item h3{font-weight:400;font-size:17px;color:var(--green);line-height:20px;margin-bottom:3px;white-space:nowrap}
.news-item .copy{line-height:12.8px}
.news-item .more{display:block;font-size:15px;margin-top:2px;color:#333}
.col-rule{top:722px;width:1px;height:107px;background:var(--rule)}

.site-footer{left:0;top:869px;width:1200px;height:89px;background:var(--footer);border-top:1px solid #ddd}
.legal{left:474px;top:917px;font-family:"Arimo",sans-serif;font-size:9.6px;color:#999;white-space:nowrap}
</style>
</head>
<body>
<header class="site-header">
  <div class="brand brand--header">Velmoran<br>Associates</div>
  <div class="abs socials" aria-label="Social links"><span></span><span></span><span></span></div>
  <div class="abs search">Search...
    <svg width="18" height="18" viewBox="0 0 18 18"><circle cx="7" cy="7" r="5" fill="none" stroke="#8cbf26" stroke-width="2"/><line x1="11" y1="11" x2="16" y2="16" stroke="#8cbf26" stroke-width="2.5"/></svg>
  </div>
  <div class="abs nav-rule"></div>
  <nav class="abs nav nav--header">
    <a class="active" href="#">HOME</a><span class="sep"></span><a href="#">ABOUT US</a><span class="sep"></span><a href="#">SERVICES</a><span class="sep"></span><a href="#">BLOG</a><span class="sep"></span><a href="#">TRADE</a><span class="sep"></span><a href="#">INVESTMENT</a><span class="sep"></span><a href="#">CONTACT US</a>
  </nav>
</header>

<section class="abs hero"></section>
<div class="abs hero-art" role="img" aria-label="Business people with laptops around a rising bar chart with an orange growth arrow" style="background:linear-gradient(180deg,rgba(235,235,240,0) 0%,#e6e6ec 55%,#d8d8de 100%)"></div>
<h2 class="abs hero-title" style="font-weight:400">Trade, Investment<span class="accent">Market Research</span></h2>
<svg class="abs arrow" style="left:160px" width="42" height="76" viewBox="0 0 42 76"><polyline points="40,1 2,38 40,75" fill="none" stroke="#999" stroke-width="1.2"/></svg>
<svg class="abs arrow" style="left:998px" width="42" height="76" viewBox="0 0 42 76"><polyline points="2,1 40,38 2,75" fill="none" stroke="#999" stroke-width="1.2"/></svg>
<div class="abs hero-shadow"></div>

<section class="abs welcome">
  <h1>Welcome to <span class="name">Velmoran <em>Associates!</em></span></h1>
  <p class="copy">Lorem ipsum dolor sit amet, consectetur adipiscing elit. Aliquam velit erat, fermentum dignissim vulputate velue laoreet facilisis, ullamcorper eu ipsum. In at vulputate ipsum, vel viverra libero. Nullam id tellus neque. aliquam Nunc vel rhoncus felis. Aliquam ut nulla odio. Praesent interdum metus vitae sollicitudin placerat interdum. Phasellus mauris ligula, tristique vitae consectetur.</p>
</section>
<div class="abs split"></div>
<p class="abs quote">Getting into a new market<br>is easier than staying in<br>that market.</p>
<div class="abs band-rule"></div>

<h2 class="abs news-title">News &amp; Events</h2>
<article class="abs news-item" style="left:200px">
  <div class="date">Jul-10-2013</div><h3>Lorem ipsum dolor sit.</h3>
  <p class="copy">Lorem ipsum dolor sit amet, consectetur adipiscing elit. Aliquam velit erat, fermentum dignissim vulputate velue laoreet facilisis, ullamcorper eu ipsum. In at vulput.</p>
  <a class="more" href="#">Read more</a>
</article>
<div class="abs col-rule" style="left:445px"></div>
<article class="abs news-item" style="left:504px">
  <div class="date">Jul-10-2013</div><h3>Lorem ipsum dolor sit.</h3>
  <p class="copy">Lorem ipsum dolor sit amet, consectetur adipiscing elit. Aliquam velit erat, fermentum dignissim vulputate velue laoreet facilisis, ullamcorper eu ipsum. In at vulput.</p>
  <a class="more" href="#">Read more</a>
</article>
<div class="abs col-rule" style="left:750px"></div>
<article class="abs news-item" style="left:809px">
  <div class="date">Jul-10-2013</div><h3>Lorem ipsum dolor sit.</h3>
  <p class="copy">Lorem ipsum dolor sit amet, consectetur adipiscing elit. Aliquam velit erat, fermentum dignissim vulputate velue laoreet facilisis, ullamcorper eu ipsum. In at vulput.</p>
  <a class="more" href="#">Read more</a>
</article>

<footer class="abs site-footer"></footer>
<div class="brand brand--footer">Velmoran<br>Associates</div>
<nav class="abs nav nav--footer">
  <a href="#">HOME</a><span class="sep"></span><a href="#">ABOUT US</a><span class="sep"></span><a href="#">SERVICES</a><span class="sep"></span><a href="#">BLOG</a><span class="sep"></span><a href="#">TRADE</a><span class="sep"></span><a href="#">INVESTMENT</a><span class="sep"></span><a href="#">CONTACT US</a>
</nav>
<p class="abs legal">Copyright © Velmoran Associates | Privacy Policy | Terms &amp; Conditions</p>
</body>
</html>
```